Duel Business card

Want an edgy business card that shows both of our companies on each side of the card, OR both together with a cool design.

*Must be edgy: We have attached our two business logos. We are a bail bond and immigration bond company.

Would like the address on one side only.
Need Phone, cell, website, address, and Name

Company Name 1: Cellgate Release Partners
www.cellgatereleasepartners.example

Company Name 2: Borderline Surety Associates
www.borderlinesuretyassociates.example

These cards will need to be easily changeable so I can modify new employees

Target Market(s)

people in jail, takign imigrants out of jail and from being taken back to there country

Industry/Entity Type

Business

Requirements
Must have
• Include both logos attached

```html
<!DOCTYPE html>
<html lang="en">
<head>
<meta charset="utf-8">
<title>Cellgate Release Partners &amp; Borderline Surety Associates – Business Card</title>
<link rel="stylesheet" href="https://fonts.googleapis.com/css2?family=Ubuntu:ital,wght@0,400;0,500;0,700;1,700&display=swap">
<style>
  :root {
    --stage: #d9d9d9;
    --card-teal: #2db6c4;
    --card-dark: #221e1f;
    --ribbon: #1c1a1b;
    --white: #ffffff;
    --navy: #1b3f8f;
    --gold: #f5c400;
    --badge-red: #d9453a;
    --shadow: rgba(0, 0, 0, 0.35);
  }
  * { box-sizing: border-box; margin: 0; padding: 0; }
  html, body { width: 1200px; height: 900px; overflow: hidden; }
  body {
    background: var(--stage);
    font-family: "Ubuntu", sans-serif;
    position: relative;
  }
  .card {
    position: absolute;
    width: 660px;
    height: 377px;
    border-radius: 4px;
    box-shadow: 0 14px 30px var(--shadow);
    overflow: hidden;
  }
  /* Front: teal contact side */
  .card-front { left: 120px; top: 60px; background: var(--card-teal); }
  .front-brands {
    position: absolute; left: 28px; top: 24px;
    display: flex; flex-direction: column; gap: 10px;
  }
  .brand {
    display: flex; align-items: center; gap: 10px;
    font-weight: 700; font-size: 17px; color: var(--white);
  }
  .brand-dot { width: 44px; height: 44px; border-radius: 50%; flex: none; }
  .brand-dot.surety { background: var(--badge-red); }
  .brand-dot.release { background: var(--navy); }
  .ribbon {
    position: absolute; left: 0; top: 168px; width: 300px; height: 84px;
  }
  .ribbon svg { position: absolute; inset: 0; }
  .ribbon-text {
    position: absolute; left: 26px; top: 10px; color: var(--white);
    font-weight: 700; font-style: italic;
  }
  .person-name { font-size: 34px; line-height: 38px; }
  .person-title { font-size: 22px; line-height: 28px; }
  .contact {
    position: absolute; right: 28px; top: 104px; text-align: right;
    color: var(--white); font-size: 17px; line-height: 25px;
  }
  .contact .label { font-size: 10px; opacity: .8; margin-left: 6px; display: inline-block; width: 46px; text-align: left; }
  .contact .web { font-size: 19px; line-height: 27px; }
  .contact .company { font-size: 19px; }

  /* Back: dark brand side */
  .card-back {
    left: 420px; top: 470px; background: var(--card-dark);
    display: flex; align-items: center; justify-content: space-around; padding: 0 30px;
  }
  .back-brand {
    display: flex; flex-direction: column; align-items: center; gap: 16px;
    font-weight: 700; text-align: center; width: 260px;
  }
  .back-brand .brand-dot { width: 150px; height: 150px; }
  .back-brand.surety .brand-dot { background: var(--badge-red); }
  .back-brand.release .brand-dot { width: 96px; height: 96px; background: var(--navy); }
  .back-brand.surety .brand-name { color: var(--white); font-size: 22px; }
  .back-brand.release .brand-name { color: var(--gold); font-size: 30px; line-height: 34px; }
</style>
</head>
<body>
  <section class="card card-front" aria-label="Card front">
    <div class="front-brands">
      <div class="brand"><span class="brand-dot surety"></span><span class="brand-name">Borderline Surety Associates</span></div>
      <div class="brand"><span class="brand-dot release"></span><span class="brand-name">Cellgate Release Partners</span></div>
    </div>

    <div class="ribbon">
      <svg width="300" height="84" viewBox="0 0 300 84" aria-hidden="true">
        <polygon points="0,0 270,0 270,50 298,74 262,64 0,64" fill="var(--ribbon)"/>
      </svg>
      <div class="ribbon-text">
        <div class="person-name">John Doe</div>
        <div class="person-title">Title</div>
      </div>
    </div>

    <div class="contact">
      <div class="company">Cellgate Release Partners</div>
      <div class="company">Borderline Surety Associates</div>
      <div>+000 123 456 789<span class="label">telephone</span></div>
      <div>+000 123 456 789<span class="label">cell</span></div>
      <div>123 John Rd. City, State, Zip<span class="label">address</span></div>
      <div class="web">www.cellgatereleasepartners.example<span class="label">web</span></div>
      <div class="web">www.borderlinesuretyassociates.example<span class="label">web</span></div>
    </div>
  </section>

  <section class="card card-back" aria-label="Card back">
    <div class="back-brand surety">
      <span class="brand-dot"></span>
      <span class="brand-name">Borderline Surety Associates</span>
    </div>
    <div class="back-brand release">
      <span class="brand-dot"></span>
      <span class="brand-name">Cellgate Release Partners</span>
    </div>
  </section>
</body>
</html>
```